Your After-Split Lantern: Sensible, Everyday Guidance for the Freshly Solo

I need a wraparound book cover design for a ~132-page workbook. Trim size will be 8.5x11 and the book will be on 60# paper. The name of this project is the name and subtitle of the book. Here's the synopsis I've come up with, which should be included on the back cover (without the quote marks):
"So you're divorced. What do you do now? There are probably a whole bunch of
things you never thought of, like:
- Cleaning up and automating your finances
- Making sure your insurance coverages are all correct
- Removing your former spouse's name from your assets and liabilities
- Building your personal team of financial advisors
Are you aware you need to take care of these things, but you don't know where to
start? This workbook is perfect for you. You'll be led, step by step, through detailed
explanations of how to do everything on this list, and much, much more!"
Here's the author bio for the back cover:
"Gregory T. Whitlock, Esq. graduated from Halvern College School of Law in 2002 and has been a practicing trial lawyer in the Metro Atlanta area ever since. Family law has always been a big part of Greg's practice. Throughout his career, Greg has helped hundreds of people through their divorce cases, and now through this book, Greg looks forward to being able to help them after the dust settles."
I have an ISBN bar code ready to go, so leave space for it on the back cover in the bottom right corner (winner will be expected to add the bar code graphic to the finished product).
This will be a print-on-demand book through Brindlemart's PressNook. They have a sizing template if you want to grab it for yourself.
Target Market(s)
Primarily divorced women, especially middle-aged and older
Look and feel
Each slider illustrates characteristics of the customer's brand and the style your logo design should communicate.

```html
<!DOCTYPE html>
<html lang="en">
<head>
<meta charset="utf-8">
<title>Your After-Split Lantern – Wraparound Cover</title>
<link rel="stylesheet" href="https://fonts.googleapis.com/css2?family=Oswald:wght@500;700&family=PT+Serif:wght@400;700&family=Roboto:wght@400&display=swap">
<style>
  :root {
    --ink: #111111;
    --paper: #ffffff;
    --photo-light: #ece6e1;
    --photo-mid: #c9b8ab;
    --photo-dark: #6b5a4f;
  }
  * { margin: 0; padding: 0; box-sizing: border-box; }
  html, body { width: 1200px; height: 776px; overflow: hidden; background: var(--paper); }
  .cover { position: relative; width: 1200px; height: 776px; background: var(--paper); color: var(--ink); font-family: "PT Serif", Georgia, serif; }

  /* Back cover */
  .back { position: absolute; left: 0; top: 0; width: 578px; height: 776px; background: var(--paper); }
  .synopsis-lead { position: absolute; left: 40px; top: 38px; width: 470px; text-align: center; font-weight: 700; font-size: 16.5px; line-height: 26px; letter-spacing: 0.3px; }
  .synopsis-list { position: absolute; left: 47px; top: 120px; width: 455px; list-style: none; font-size: 16px; line-height: 22.5px; }
  .synopsis-close { position: absolute; left: 47px; top: 233px; width: 455px; font-size: 16px; line-height: 22.5px; text-align: justify; }
  .author-band { position: absolute; left: 0; top: 355px; width: 578px; height: 52px; background: var(--ink); color: var(--paper); font-family: "Oswald", "Arial Narrow", sans-serif; font-weight: 700; font-size: 37px; line-height: 52px; text-align: center; letter-spacing: 0.5px; }
  .author-bio { position: absolute; left: 47px; top: 415px; width: 455px; font-size: 16px; line-height: 22.5px; text-align: justify; }
  .barcode-space { position: absolute; left: 337px; top: 629px; width: 164px; height: 103px; background: var(--ink); }

  /* Spine */
  .spine { position: absolute; left: 578px; top: 0; width: 43px; height: 776px; background: var(--ink); color: var(--paper); }
  .spine-title { position: absolute; left: 0; top: 30px; width: 43px; writing-mode: vertical-rl; font-family: "Oswald", "Arial Narrow", sans-serif; font-weight: 700; font-size: 21px; letter-spacing: 2.2px; line-height: 43px; text-align: left; }
  .spine-author { position: absolute; left: 0; top: 436px; width: 43px; writing-mode: vertical-rl; font-size: 27px; line-height: 43px; }

  /* Front cover */
  .front { position: absolute; left: 621px; top: 0; width: 579px; height: 776px; background: var(--ink); color: var(--paper); }
  .front-photo { position: absolute; left: 0; top: 0; width: 579px; height: 420px; background: linear-gradient(135deg, var(--photo-dark) 0%, var(--photo-mid) 30%, var(--photo-light) 60%, var(--paper) 100%); }
  .title { position: absolute; left: 0; top: 428px; width: 579px; text-align: center; }
  .title-lead { display: block; font-family: "Roboto", Arial, sans-serif; font-size: 42px; line-height: 50px; }
  .title-main { display: block; font-family: "Oswald", "Arial Narrow", sans-serif; font-weight: 700; font-size: 74px; line-height: 76px; letter-spacing: -0.5px; }
  .title-word { display: block; font-family: "Oswald", "Arial Narrow", sans-serif; font-weight: 700; font-size: 78px; line-height: 80px; letter-spacing: 22px; padding-left: 22px; }
  .subtitle { position: absolute; left: 0; top: 648px; width: 579px; text-align: center; font-size: 19px; }
  .front-author { position: absolute; left: 0; top: 712px; width: 579px; text-align: center; font-size: 35px; }
</style>
</head>
<body>
<main class="cover">
  <section class="back">
    <p class="synopsis-lead">SO YOU'RE DIVORCED. WHAT DO YOU DO NOW?<br>THERE ARE PROBABLY A WHOLE BUNCH OF<br>THINGS YOU NEVER THOUGHT OF, LIKE:</p>
    <ul class="synopsis-list">
      <li>- Cleaning up and automating your finances</li>
      <li>- Making sure your insurance coverages are all correct</li>
      <li>- Removing your former spouse's name from your assets and liabilities.</li>
      <li>- Building your personal team of financial advisors</li>
    </ul>
    <p class="synopsis-close">Are you aware you need to take care of these things, but you don't know where to start? This workbook is perfect for you. You'll be led, step by step, through detailed explanations of how to do everything on this list, and much, much more.</p>
    <h2 class="author-band">ABOUT THE AUTHOR</h2>
    <p class="author-bio">Gregory T. Whitlock, Esq. graduated from Halvern College School of Law in 2002 and has been a practicing trial lawyer in the Metro Atlanta area ever since. Family law has always been a big part of Greg's practice. Throughout his career, Greg has helped hundreds of people through their divorce cases, and now through this book, Greg looks forward to being able to help them after the dust settles.</p>
    <div class="barcode-space"></div>
  </section>

  <aside class="spine">
    <span class="spine-title">YOUR AFTER-SPLIT LANTERN</span>
    <span class="spine-author">Gregory T. Whitlock</span>
  </aside>

  <section class="front">
    <div class="front-photo" role="img" aria-label="Photo of a frustrated woman in glasses biting a divorce application form"></div>
    <h1 class="title">
      <span class="title-lead">Your</span>
      <span class="title-main">AFTER-SPLIT</span>
      <span class="title-word">LANTERN</span>
    </h1>
    <p class="subtitle">Sensible, Everyday Guidance for the Freshly Solo</p>
    <p class="front-author">Gregory T. Whitlock</p>
  </section>
</main>
</body>
</html>
```